Flyer-Design für Immobilienmakler
Zielgruppe
Wir sind seit 1992 Immobilienmakler und möchten einen Flyer zur Präsentation unserer Firma und Objektakquise gestalten lassen.
Dieser soll einen Gutschein für eine kostenlose Immobilienbewertung enthalten.
Aufgabenstellung
Wir lassen uns dann überraschen

```html
<!DOCTYPE html>
<html lang="de">
<head>
<meta charset="utf-8">
<title>Gutschein – Kostenlose Immobilienbewertung</title>
<link href="https://fonts.googleapis.com/css2?family=Michroma&family=Montserrat:wght@300;400;700;800;900&family=Oswald:wght@300;400&display=swap" rel="stylesheet">
<style>
  :root{
    --paper:#ffffff;
    --frame:#6b6c6e;
    --panel:#6f7072;
    --dark:#2b2b2c;
    --ink:#6d6e70;
    --red:#e84a4a;
    --red-deep:#e31e24;
    --white:#ffffff;
  }
  *{margin:0;padding:0;box-sizing:border-box}
  html,body{width:874px;height:1200px;overflow:hidden;background:var(--paper)}
  .flyer{position:relative;width:874px;height:1200px;background:var(--paper);font-family:"Montserrat",sans-serif}
  .crop-marks{position:absolute;inset:0}
  .voucher{position:absolute;left:22px;top:22px;width:829px;height:362px;background:var(--frame)}
  .voucher__topbar{position:absolute;left:24px;top:12px;width:781px;height:12px;background:var(--dark);border-bottom:2px solid var(--red)}
  .voucher__photo{position:absolute;left:24px;top:24px;width:310px;height:280px;
    background:linear-gradient(160deg,#dfe6ea 0%,#c9b3a0 38%,#a86a4a 55%,#e9e9e9 80%,#f4f4f4 100%)}
  .voucher__panel{position:absolute;left:334px;top:24px;width:471px;height:280px;background:var(--panel);color:var(--white);font-family:"Michroma",sans-serif}
  .voucher__title{position:absolute;left:26px;top:20px;font-family:"Michroma",sans-serif;font-weight:700;font-size:29px;letter-spacing:3px;-webkit-text-stroke:1px var(--white)}
  .voucher__text{position:absolute;left:28px;font-size:15px;line-height:22px;letter-spacing:1.2px}
  .voucher__text--offer{top:88px;font-weight:700;-webkit-text-stroke:.4px var(--white)}
  .voucher__text--type{top:154px;-webkit-text-stroke:.4px var(--white)}
  .voucher__text--call{top:218px;font-size:15px}
  .voucher__phone{position:absolute;left:110px;top:234px;display:flex;align-items:center;gap:8px;font-family:"Montserrat",sans-serif;font-weight:800;font-size:37px;letter-spacing:-1.5px}
  .voucher__redline{position:absolute;left:24px;top:304px;width:781px;height:2px;background:var(--red)}
  .voucher__band{position:absolute;left:24px;top:306px;width:781px;height:56px;background:var(--dark)}
  .voucher__tab{position:absolute;top:318px;width:22px;height:44px;background:var(--red)}
  .voucher__tab--left{left:0}
  .voucher__tab--right{right:0}

  .hero{position:absolute;left:22px;top:384px;width:829px;height:456px;overflow:hidden;
    background:radial-gradient(ellipse at 58% 45%,#5a5a5b 0%,#3a3a3b 45%,#222 100%)}
  .hero__figure{position:absolute;left:330px;top:16px;width:270px;height:440px;border-radius:120px 120px 0 0;
    background:linear-gradient(180deg,#4a3428 0%,#6b4a3a 22%,#cbb9a2 45%,#d6c7b2 100%)}
  .hero__word{position:absolute;color:var(--white);font-family:"Montserrat",sans-serif;font-weight:800;transform-origin:left top}
  .hero__word--immo{left:68px;top:46px;font-size:32px;transform:rotate(18deg)}
  .hero__word--akq{left:62px;top:140px;font-size:21px;transform:rotate(-12deg)}
  .hero__word--power{left:98px;top:249px;font-size:16px;transform:rotate(10deg)}
  .hero__word--profit{left:695px;top:32px;font-size:19px;transform:rotate(8deg)}
  .hero__word--success{left:680px;top:98px;font-size:23px;transform:rotate(-18deg)}

  .badge{position:absolute;left:556px;top:630px;width:256px;height:256px}
  .badge__text{position:absolute;inset:0;transform:rotate(14deg);color:var(--white);text-align:center}
  .badge__pct{position:absolute;left:0;right:0;top:50px;font-weight:900;font-size:60px;letter-spacing:-2px}
  .badge__off{position:absolute;left:0;right:0;top:100px;font-weight:900;font-size:78px;letter-spacing:-3px}
  .badge__note{position:absolute;left:0;right:0;top:184px;font-weight:800;font-size:18px}

  .pitch{position:absolute;left:53px;top:858px;color:var(--ink);font-weight:300;font-size:35.5px;line-height:34px;letter-spacing:-.3px}
  .pitch__strong{color:var(--red-deep);font-weight:700;letter-spacing:-.8px}
  .invite{position:absolute;left:0;width:874px;top:982px;text-align:center;color:var(--ink);font-weight:400;font-size:21.5px}
  .tagline{position:absolute;left:0;width:874px;top:1002px;text-align:center;font-family:"Oswald",sans-serif;font-weight:300;font-size:21px;color:var(--red-deep)}
  .tagline__stroke{position:absolute;left:332px;top:1029px}

  .footer{position:absolute;left:22px;top:1048px;width:829px;height:130px;background:var(--frame);color:var(--white)}
  .footer__web{position:absolute;left:78px;top:62px;font-size:13px;font-weight:400}
  .footer__cta{position:absolute;left:482px;top:22px;font-size:19px;font-weight:400}
  .footer__cta em{font-style:normal;font-weight:700;color:var(--red)}
  .footer__phone{position:absolute;left:466px;top:46px;display:flex;align-items:center;gap:6px;font-weight:800;font-size:40px;letter-spacing:-1.5px}
</style>
</head>
<body>
<div class="flyer">
  <svg class="crop-marks" width="874" height="1200" aria-hidden="true">
    <g stroke="#555" stroke-width=".6">
      <line x1="44" y1="10" x2="44" y2="22"/><line x1="10" y1="44" x2="22" y2="44"/>
      <line x1="830" y1="10" x2="830" y2="22"/><line x1="852" y1="44" x2="864" y2="44"/>
      <line x1="44" y1="1178" x2="44" y2="1190"/><line x1="10" y1="1156" x2="22" y2="1156"/>
      <line x1="830" y1="1178" x2="830" y2="1190"/><line x1="852" y1="1156" x2="864" y2="1156"/>
    </g>
  </svg>

  <section class="voucher">
    <div class="voucher__topbar"></div>
    <div class="voucher__photo" role="img" aria-label="Foto: Lupe über einem modernen Haus auf Bauplänen"></div>
    <div class="voucher__panel">
      <h1 class="voucher__title">GUTSCHEIN</h1>
      <p class="voucher__text voucher__text--offer">für eine kostenlose<br>Bewertung Ihrer Immobilie.</p>
      <p class="voucher__text voucher__text--type">Egal ob<br>Haus oder Wohnung</p>
      <p class="voucher__text voucher__text--call">Wir freuen uns auf Ihren<br>Anruf.</p>
      <div class="voucher__phone">
        <svg width="50" height="30" viewBox="0 0 50 30" aria-hidden="true"><path d="M3 12c0-6 10-10 22-10s22 4 22 10l-1 4h-10v-5c-6-2-16-2-22 0v5H4z" fill="#fff"/><ellipse cx="25" cy="22" rx="17" ry="8" fill="#fff"/><circle cx="25" cy="21" r="5" fill="#6f7072"/></svg>
        <span>1800 555 019</span>
      </div>
    </div>
    <div class="voucher__redline"></div>
    <div class="voucher__band"></div>
    <div class="voucher__tab voucher__tab--left"></div>
    <div class="voucher__tab voucher__tab--right"></div>
  </section>

  <section class="hero">
    <div class="hero__figure" role="img" aria-label="Foto: Maklerin im hellen Anzug mit Laptop vor einer Kreidetafel"></div>
    <span class="hero__word hero__word--immo">Immobilien</span>
    <span class="hero__word hero__word--akq">Akquise</span>
    <span class="hero__word hero__word--power">Power</span>
    <span class="hero__word hero__word--profit">Profit</span>
    <span class="hero__word hero__word--success">Success</span>
  </section>

  <div class="badge">
    <svg width="256" height="256" viewBox="0 0 256 256" aria-hidden="true">
      <polygon fill="#e84a4a" points="128,4 150,34 184,18 191,55 228,56 218,92 250,110 225,138 245,170 209,178 206,215 170,208 150,242 128,216 104,250 88,214 50,222 50,184 14,172 36,140 8,112 42,96 34,58 72,58 80,20 112,38"/>
    </svg>
    <div class="badge__text">
      <div class="badge__pct">20%</div>
      <div class="badge__off">OFF</div>
      <div class="badge__note">Special Offer!</div>
    </div>
  </div>

  <p class="pitch">Verkaufen Sie Ihr Eigentum nicht "unter Wert"<br>sondern lassen Sie Ihre Immobilie von uns<br><span class="pitch__strong">kostenlos und realistisch bewerten.</span></p>
  <p class="invite">Vereinbaren Sie ein unverbindliches Kennenlerngespräch mit uns unter</p>
  <p class="tagline">Business off the ground.</p>
  <svg class="tagline__stroke" width="226" height="8" viewBox="0 0 226 8" aria-hidden="true"><path d="M2 5 C60 1 150 7 224 3" stroke="#e31e24" stroke-width="2.5" fill="none" stroke-linecap="round"/></svg>

  <footer class="footer">
    <span class="footer__web">www.wertkompass-immo.de</span>
    <span class="footer__cta">Call Now <em>Limited</em> Time Offer!</span>
    <div class="footer__phone">
      <svg width="52" height="32" viewBox="0 0 50 30" aria-hidden="true"><path d="M3 12c0-6 10-10 22-10s22 4 22 10l-1 4h-10v-5c-6-2-16-2-22 0v5H4z" fill="#fff"/><ellipse cx="25" cy="22" rx="17" ry="8" fill="#fff"/><circle cx="25" cy="21" r="5" fill="#6b6c6e"/></svg>
      <span>1800 555 019</span>
    </div>
  </footer>
</div>
</body>
</html>
```